Business Card Design

We recently had a new logo designed by Pixel Harbor. Now we want to create new business cards and letterhead that compliment our new logo.

We are audiologists in private practice specializing in hearing evaluations and fitting hearing aids. We want a clean and professional card.

We need business cards for each audiologist. The names and titles are:
Marnie Ostrova, AuD
Audiologist

Jen Tarbel, AuD
Audiologist

Corvina Plesk, AuD
Audiologist

We also need a business card with no provider. Just a generic one.

Finally, we need an appointment card. This is what the front desk uses to give to the patient with their next appointment date and time.

Target Market(s)

Our clients tend to be highly educated. They are older so the cards should be clean and easy to read. No squirrely font please.

Industry/Entity Type

Business

Contact Information for Business Card

20731 8th Ave NE, suite 417
Seattle, WA 98177
206-592-8074

Requirements
Must have
• Clean
Easy to read
Professional
Modern but approachable / warm
Should not have
• Other pictures besides the logo

```html
<!DOCTYPE html>
<html lang="en">
<head>
<meta charset="utf-8">
<title>Eastbrook Hearing Services – Business Card</title>
<link rel="stylesheet" href="https://fonts.googleapis.com/css2?family=Arimo:wght@400;700&display=swap">
<style>
  :root {
    --backdrop: #173f5f;
    --card: #ffffff;
    --navy: #1b3e5e;
    --teal: #3aa893;
    --grey-text: #444444;
    --divider: #6b6b6b;
  }
  * { margin: 0; padding: 0; box-sizing: border-box; }
  html, body {
    width: 1200px;
    height: 862px;
    overflow: hidden;
    background: var(--backdrop);
    font-family: "Arimo", Arial, sans-serif;
  }
  .canvas {
    position: relative;
    width: 1200px;
    height: 862px;
  }
  .business-card {
    position: absolute;
    left: 207px;
    top: 225px;
    width: 767px;
    height: 436px;
    background: var(--card);
  }
  .brand {
    position: absolute;
    left: 54px;
    top: 117px;
    display: flex;
    align-items: center;
    gap: 18px;
  }
  .brand-dot {
    width: 88px;
    height: 88px;
    border-radius: 50%;
    background: var(--teal);
    flex: none;
  }
  .brand-name {
    color: var(--navy);
    font-weight: 700;
    line-height: 1.15;
  }
  .brand-name .primary { display: block; font-size: 36px; letter-spacing: 0.5px; }
  .brand-name .secondary { display: block; font-size: 19px; letter-spacing: 1.5px; text-transform: uppercase; }
  .divider {
    position: absolute;
    left: 441px;
    top: 113px;
    width: 2px;
    height: 114px;
    background: var(--divider);
  }
  .provider {
    position: absolute;
    left: 457px;
    top: 135px;
  }
  .provider-name {
    color: var(--navy);
    font-weight: 700;
    font-size: 27px;
    line-height: 1.2;
  }
  .provider-title {
    color: var(--teal);
    font-weight: 400;
    font-size: 27px;
    line-height: 1.2;
    margin-top: 4px;
  }
  .contact {
    position: absolute;
    left: 0;
    right: 0;
    top: 336px;
    text-align: center;
    font-size: 20px;
  }
  .contact-address {
    color: var(--grey-text);
  }
  .contact-lines {
    margin-top: 9px;
    color: var(--navy);
    font-weight: 700;
  }
  .contact-lines .sep {
    color: var(--teal);
    margin: 0 8px;
    font-weight: 400;
  }
  .contact-lines .web {
    color: var(--teal);
  }
</style>
</head>
<body>
<main class="canvas">
  <section class="business-card">
    <div class="brand">
      <span class="brand-dot"></span>
      <p class="brand-name">
        <span class="primary">Eastbrook</span>
        <span class="secondary">Hearing Services</span>
      </p>
    </div>
    <span class="divider"></span>
    <div class="provider">
      <p class="provider-name">Marnie Ostrova, AuD</p>
      <p class="provider-title">Audiologist</p>
    </div>
    <div class="contact">
      <p class="contact-address">20731 8th Ave NE, suite 417 Seattle, WA 98177 206-592-8074</p>
      <p class="contact-lines">Tel: 089 5550162<span class="sep">|</span>Fax: 089 5550167<span class="sep">|</span><span class="web">www.eastbrook.com</span></p>
    </div>
  </section>
</main>
</body>
</html>
```